Business Card for Fashion House

We need a business card design for our personalize fashion service for our customers. the business card should reflect reliability, luxury and creativity.
The brand Vastrelle is extracted from "Vibrant Estrella"; Vastrelle provides fashion designs sprinkled with luxury and style tailored for our elite clients character profile.
Vastrelle is created for those who embody class and elegance with a passion for style.
Target Market(s)
Affluent Customers
Industry/Entity Type
Fashion
Contact Information for Business Card
Noura Al Hashimi
Fashion Designer
Telephone: +971 5550192
Mobile +971 555073
Emal q@k.example
Website www.vastrelle.example
Social Media Youtube g+ Facebook Instagram Pin /vastrelle
Font styles to use
Other font styles liked:
- Audrey provided
Look and feel
Each slider illustrates characteristics of the customer's brand and the style your logo design should communicate.

```html
<!DOCTYPE html>
<html lang="en">
<head>
<meta charset="utf-8">
<title>Vastrelle Business Card</title>
<link rel="stylesheet" href="https://fonts.googleapis.com/css2?family=Marcellus&display=swap">
<style>
  :root {
    --backdrop: #3b3431;
    --card: #141414;
    --card-edge: #1f1f1f;
    --ink: #f2f2f2;
    --ink-soft: #cfcfcf;
    --rule: #8a8a8a;
  }
  * { margin: 0; padding: 0; box-sizing: border-box; }
  html, body {
    width: 1200px; height: 780px; overflow: hidden;
    background: var(--backdrop);
    font-family: "Marcellus", "Optima", serif;
    color: var(--ink);
  }
  .canvas {
    width: 1200px; height: 780px;
    display: flex; align-items: center; justify-content: center; gap: 40px;
  }
  .card {
    width: 540px; height: 308px;
    background: linear-gradient(150deg, var(--card-edge), var(--card));
    border-radius: 4px;
    box-shadow: 0 14px 30px rgba(0,0,0,.45);
    position: relative;
  }
  /* Front */
  .card--front {
    display: flex; flex-direction: column; align-items: center; justify-content: center;
  }
  .brand { display: flex; flex-direction: column; align-items: center; }
  .brand__dot {
    width: 44px; height: 44px; border: 2px solid var(--ink); border-radius: 50%;
    margin-bottom: 16px;
  }
  .brand__name {
    font-size: 24px; letter-spacing: 0.5em; margin-right: -0.5em;
    text-transform: uppercase;
  }
  .social {
    margin-top: 22px; display: flex; align-items: center; gap: 8px;
    font-size: 15px; letter-spacing: 0.08em; color: var(--ink-soft);
  }
  .social__dot {
    width: 14px; height: 14px; border: 1.5px solid var(--ink-soft); border-radius: 50%;
  }
  /* Back */
  .card--back { display: flex; align-items: center; }
  .card--back .brand { width: 250px; }
  .card--back .brand__name { font-size: 21px; }
  .divider {
    width: 1px; height: 128px; background: var(--rule);
  }
  .contact { padding-left: 26px; }
  .contact__name { font-size: 19px; letter-spacing: 0.03em; }
  .contact__role { font-size: 13px; color: var(--ink-soft); margin-bottom: 12px; }
  .contact__list { list-style: none; }
  .contact__item {
    display: flex; align-items: center; gap: 8px;
    font-size: 14px; line-height: 23px; letter-spacing: 0.04em;
  }
  .contact__icon { width: 16px; height: 16px; flex: none; }
  .contact__web { font-size: 13px; letter-spacing: 0.1em; margin-top: 4px; }
</style>
</head>
<body>
<main class="canvas">
  <section class="card card--front">
    <div class="brand">
      <span class="brand__dot"></span>
      <span class="brand__name">Vastrelle</span>
    </div>
    <div class="social">
      <span class="social__dot"></span>
      <span>/vastrelle</span>
    </div>
  </section>

  <section class="card card--back">
    <div class="brand">
      <span class="brand__dot"></span>
      <span class="brand__name">Vastrelle</span>
    </div>
    <span class="divider"></span>
    <div class="contact">
      <p class="contact__name">Noura Al Hashimi</p>
      <p class="contact__role">Fashion Designer</p>
      <ul class="contact__list">
        <li class="contact__item">
          <svg class="contact__icon" viewBox="0 0 16 16" fill="none" stroke="currentColor" stroke-width="1.2">
            <circle cx="8" cy="8" r="7.3"/>
            <path d="M5.2 4.3l1.4 1.6-.8 1.1c.6 1.3 1.5 2.2 2.8 2.8l1.1-.8 1.6 1.4-.9 1.2c-3-.6-5.2-2.8-5.8-5.8z"/>
          </svg>
          +971 5550192
        </li>
        <li class="contact__item">
          <svg class="contact__icon" viewBox="0 0 16 16" fill="none" stroke="currentColor" stroke-width="1.2">
            <circle cx="8" cy="8" r="7.3"/>
            <rect x="5.6" y="3.8" width="4.8" height="8.4" rx="0.8"/>
            <path d="M7.3 10.8h1.4"/>
          </svg>
          +971 555073
        </li>
        <li class="contact__item">
          <svg class="contact__icon" viewBox="0 0 16 16" fill="none" stroke="currentColor" stroke-width="1.2">
            <circle cx="8" cy="8" r="7.3"/>
            <rect x="4" y="5.3" width="8" height="5.4"/>
            <path d="M4 5.3l4 3 4-3"/>
          </svg>
          q@k.example
        </li>
        <li class="contact__item contact__web">
          <svg class="contact__icon" viewBox="0 0 16 16" fill="none" stroke="currentColor" stroke-width="1.2">
            <circle cx="8" cy="8" r="7.3"/>
            <ellipse cx="8" cy="8" rx="2.8" ry="7.3"/>
            <path d="M0.7 8h14.6M2 4.5h12M2 11.5h12"/>
          </svg>
          www.vastrelle.example
        </li>
      </ul>
    </div>
  </section>
</main>
</body>
</html>
```